Cat-products company needs smart, yet endearing, business card

We need a business card design for a new, but up-and-running, business based in Honolulu, Hawaii. The business is Purrlane Nest Co. Our first product is the most environmentally-friendly cat grass kit ever seen on the planet. Future products, currently in the R&D phase, will include a variety of exciting cat scratchers. We also do consulting work to help apartment-dwellers make their home more cat-friendly and, in the future, plan on doing full, custom installs of structure to create high walkways for cats.

Target Market(s)

Middle-aged, apartment-dwelling, middle-class workers who own 1 or more cats and who dote on them.

Industry/Entity Type

Pet Care

Contact Information for Business Card

A striking, professional, yet warm and friendly design is what we're after.

Font styles to use
Serif
Sans Serif
Other font styles liked:
• Comfortaa

Colors

Designer to choose colors to be used in the design.

Requirements
Must have
• The company logo: (see attachment)
• The company name: Purrlane Nest Co
• The web address: www.purrlanenestco.example
• Email: support@purrlanenestco.example
• Phone: +1 (808) 555 0172
• Update (Fri Jun 30 3017 7:45pm Hawaii Time) I would like, is possible, uploaded picture of the cat grass kit on the back of the card with some text along the lines of: Purrlane Nest Co - Where The Freshest Kitty Sprouts Begin
Nice to have
• A cat picture, cartoon, real or silhouette that illustrates cats in action and/or relaxing; ie using the apartment space to live, play and relax in and being well-contented.
• Most of the website is done in the font: Comfortaa. It might be nice to continue using this for brand consistency.
Should not have
• Hard-to-read fonts.

```html
<!DOCTYPE html>
<html lang="en">
<head>
<meta charset="utf-8">
<title>Purrlane Nest Co — Business Card</title>
<link rel="stylesheet" href="https://fonts.googleapis.com/css2?family=Mulish:wght@400;700&display=swap">
<style>
  :root {
    --backdrop: #2b2b2b;
    --cocoa: #533128;
    --marigold: #f2ae06;
    --paper: #f3f3f1;
    --cream: #f7f6f3;
    --ink-light: #ffffff;
    --social-dot: #7a5a50;
    --fur-orange: #c9762f;
    --fur-cream: #efe3d3;
  }
  * { box-sizing: border-box; margin: 0; padding: 0; }
  html, body {
    width: 1200px; height: 960px; overflow: hidden;
    background: var(--backdrop);
    font-family: "Mulish", sans-serif;
  }
  .card {
    position: absolute;
    width: 600px; height: 342px;
    border-radius: 18px;
    overflow: hidden;
  }
  .card-front { left: 314px; top: 114px; background: var(--cocoa); }
  .card-back { left: 311px; top: 473px; background: var(--paper); }

  .front-shapes { position: absolute; inset: 0; }

  .person { position: absolute; left: 36px; top: 46px; }
  .person-name {
    color: var(--marigold); font-weight: 700; font-size: 22px; letter-spacing: 0.2px;
  }
  .person-role { color: var(--ink-light); font-size: 15px; margin-top: 4px; margin-left: -1px; }

  .contact {
    position: absolute; left: 37px; top: 163px;
    color: var(--ink-light); font-size: 15px; line-height: 18.5px;
  }
  .contact-address { margin-bottom: 11px; }
  .contact-label { color: var(--marigold); font-weight: 700; }

  .social-dots { position: absolute; left: 37px; top: 281px; display: flex; gap: 3px; }
  .social-dots span {
    width: 29px; height: 29px; border-radius: 50%; background: var(--social-dot);
  }

  .brand {
    position: absolute; left: 300px; top: 105px; width: 250px;
    display: flex; flex-direction: column; align-items: center;
  }
  .brand-dot {
    width: 44px; height: 44px; border-radius: 50%; background: var(--cocoa); margin-bottom: 22px;
  }
  .brand-name {
    color: var(--marigold); font-weight: 700; font-size: 27px; text-align: center; line-height: 1.15;
  }

  .back-web {
    position: absolute; left: 0; right: 0; top: 86px;
    text-align: center; color: var(--marigold); font-size: 21px; font-weight: 700; letter-spacing: 1px;
  }
  .back-photo {
    position: absolute; left: 0; right: 0; top: 172px; bottom: 0;
    background: linear-gradient(100deg, var(--fur-orange) 0%, var(--fur-cream) 45%, var(--fur-orange) 70%, var(--fur-cream) 100%);
  }
</style>
</head>
<body>
  <section class="card card-front" aria-label="Business card front">
    <svg class="front-shapes" width="600" height="342" viewBox="0 0 600 342" aria-hidden="true">
      <polygon points="428,0 600,0 600,342 428,342" fill="var(--marigold)"/>
      <path d="M428,2 L598,152 Q602,168 590,168 L550,168 L550,342 L300,342 L300,168 L260,168 Q246,166 256,156 Z" fill="var(--cream)"/>
    </svg>

    <div class="person">
      <p class="person-name">MARA KEALA</p>
      <p class="person-role">CEO/FOUNDER</p>
    </div>

    <div class="contact">
      <p class="contact-address">4120 Halia Street<br>Honolulu, Hawaii 96815</p>
      <p><span class="contact-label">P:</span> +1 (808) 555 0172</p>
      <p>support@purrlanenestco.example</p>
      <p>www.purrlanenestco.example</p>
    </div>

    <div class="social-dots" aria-hidden="true"><span></span><span></span><span></span><span></span></div>

    <div class="brand">
      <span class="brand-dot" aria-hidden="true"></span>
      <p class="brand-name">Purrlane<br>Nest Co</p>
    </div>
  </section>

  <section class="card card-back" aria-label="Business card back">
    <p class="back-web">purrlanenestco.example</p>
    <div class="back-photo" role="img" aria-label="Photo of a relaxed orange and white cat lying along the bottom of the card"></div>
  </section>
</body>
</html>
```